Innovative Consulting Firm Needs New Business Cards and Stationary

Our Innovative Consulting Firm, Larkfield Consulting, is in need of new business cards and stationary designs. We want two-sided cards that incorporate our logo, which is attached. We are looking for something not too formal, but is professional and slick.

Card should have the following information:
Name (ex. Tom Bradley)
Title (ex. Manager)
Address (ex. 24680 Cedar Lane)
Address 2 (ex. Suite 100)
City
State
Zip Code
Mobile
Email

The card should also have our website: www.larkfieldconsulting.example

Industry/Entity Type

Management Consulting

Contact Information for Business Card

Name (ex. Tom Bradley)
Title (ex. Manager)
Address 2 (ex. Suite 100)
City
State
Zip Code
Mobile
Email

Font styles to use
Sans Serif

Requirements
Must have
• The colors on the card must match the colors in the logo. The exact color codes are attached in a pdf.
Nice to have
• The Company's Tagline is "Focused on your Future". This might be nice to incorporate, but not necessary.

```html
<!DOCTYPE html>
<html lang="en">
<head>
<meta charset="utf-8">
<title>Larkfield Consulting Stationery</title>
<link href="https://fonts.googleapis.com/css2?family=Open+Sans:wght@400;600;700&display=swap" rel="stylesheet">
<style>
:root{
  --navy:#1b4d7a;
  --gold:#f5ac1b;
  --paper:#ffffff;
  --backdrop:#3b3b3b;
  --ink-light:#ffffff;
}
*{margin:0;padding:0;box-sizing:border-box}
html,body{width:1200px;height:927px;overflow:hidden;background:var(--backdrop);font-family:"Open Sans",sans-serif}
.stage{position:relative;width:1200px;height:927px}

.letterhead{position:absolute;left:209px;top:100px;width:505px;height:709px;background:var(--paper);box-shadow:0 6px 18px rgba(0,0,0,.45)}
.letterhead .header-art{position:absolute;left:0;top:0;width:505px;height:142px}
.letterhead .brand{position:absolute;left:26px;top:24px;color:var(--ink-light);font-size:19px;font-weight:600;letter-spacing:.3px}
.letterhead .contact{position:absolute;right:26px;top:22px;text-align:right;color:var(--ink-light);font-size:8.4px;line-height:10.6px}
.contact .name{font-size:11.5px;font-weight:700;line-height:14px}
.contact .title{color:var(--gold);margin-bottom:6px}
.contact .address{margin-bottom:5px}
.contact .line{display:flex;justify-content:flex-end;align-items:center;gap:6px}
.icon{display:inline-block;width:7px;height:7px;border:1px solid currentColor;border-radius:50%}

.card{position:absolute;width:211px;height:121px;border-radius:5px;overflow:hidden;box-shadow:0 6px 16px rgba(0,0,0,.5)}
.card-front{left:780px;top:112px;background:var(--paper)}
.card-front .card-art{position:absolute;left:0;top:0;width:211px;height:121px}
.card-front .name{position:absolute;left:11px;top:9px;color:var(--navy);font-size:7px;font-weight:700;line-height:8px}
.card-front .title{position:absolute;left:11px;top:17px;color:var(--gold);font-size:4.4px}
.card-front .brand{position:absolute;right:10px;top:10px;color:var(--navy);font-size:9px;font-weight:600}
.card-front .contact-block{position:absolute;left:11px;top:74px;color:var(--ink-light);font-size:4.3px;line-height:5.6px}
.card-front .contact-block .address{margin-bottom:2px}
.card-front .contact-block .line{display:flex;align-items:center;gap:4px}
.card-front .contact-block .icon{width:5px;height:5px;color:var(--gold)}
.card-front .web{color:var(--gold)}

.card-back{left:781px;top:293px;background:var(--navy);display:flex;align-items:center;justify-content:center}
.card-back .brand{color:var(--ink-light);font-size:13px;font-weight:600}
</style>
</head>
<body>
<div class="stage">
  <section class="letterhead">
    <svg class="header-art" viewBox="0 0 505 142" aria-hidden="true">
      <path d="M0 0H505V136C330 138 110 120 0 62Z" fill="var(--navy)"/>
      <path d="M0 64C110 122 330 140 505 138C330 142 100 130 0 92Z" fill="var(--gold)"/>
      <path d="M0 62C110 120 330 138 505 136L505 138C330 140 110 122 0 64Z" fill="#ffffff"/>
    </svg>
    <div class="brand">Larkfield Consulting</div>
    <div class="contact">
      <div class="name">Tom Bradley</div>
      <div class="title">Account Executive</div>
      <div class="address">24680 Cedar Lane | P.O. Box 412,<br>Suite 100 Springfield, NY 10000</div>
      <div class="line">555.014.2290 <span class="icon"></span></div>
      <div class="line">tom_bradley@larkfield.example <span class="icon"></span></div>
      <div class="line">www.larkfieldconsulting.example <span class="icon"></span></div>
    </div>
  </section>

  <section class="card card-front">
    <svg class="card-art" viewBox="0 0 211 121" aria-hidden="true">
      <path d="M0 56C80 56 160 62 211 74V121H0Z" fill="var(--gold)"/>
      <path d="M0 58C80 58 160 66 211 77V121H0Z" fill="#ffffff"/>
      <path d="M0 60C80 60 160 68 211 79V121H0Z" fill="var(--navy)"/>
    </svg>
    <div class="name">Tom Bradley</div>
    <div class="title">Account Executive</div>
    <div class="brand">Larkfield Consulting</div>
    <div class="contact-block">
      <div class="address">24680 Cedar Lane | P.O. Box 412,<br>Suite 100 Springfield, NY 10000</div>
      <div class="line"><span class="icon"></span>555.014.2290</div>
      <div class="line"><span class="icon"></span>tom_bradley@larkfield.example</div>
      <div class="line"><span class="icon"></span><span class="web">www.larkfieldconsulting.example</span></div>
    </div>
  </section>

  <section class="card card-back">
    <div class="brand">Larkfield Consulting</div>
  </section>
</div>
</body>
</html>
```